Director of a child care centre business card

Corinne Helbrook - Director/ Owner
418 Fernlow Rd
Kelmont, 3178
Phone - 03 9581-4726
Fax - 03 95814727
info@tinybrambles.com.au
www.tinybrambles.com.au

Also needing another card same information but the name will be Yvette Colder - Centre Director

```html
<!DOCTYPE html>
<html lang="en">
<head>
<meta charset="utf-8">
<title>Tiny Brambles – Business Card</title>
<link rel="stylesheet" href="https://fonts.googleapis.com/css2?family=Ubuntu:wght@300;400;500;700&display=swap">
<style>
  :root {
    --backdrop: #d9d9d7;
    --navy: #12355f;
    --pink: #dd1a7e;
    --paper: #f3f3f1;
    --ink: #3a3a3a;
    --white: #ffffff;
    --shadow: rgba(0, 0, 0, 0.18);
  }
  * { box-sizing: border-box; margin: 0; padding: 0; }
  html, body {
    width: 1200px;
    height: 1000px;
    overflow: hidden;
    background: var(--backdrop);
    font-family: "Ubuntu", sans-serif;
  }
  .canvas {
    position: relative;
    width: 1200px;
    height: 1000px;
  }
  .card {
    position: absolute;
    width: 630px;
    height: 360px;
    border-radius: 3px;
    box-shadow: 0 10px 24px var(--shadow);
    overflow: hidden;
  }

  /* Front side */
  .card-front {
    left: 480px;
    top: 90px;
    background: var(--navy);
    display: flex;
    flex-direction: column;
    align-items: center;
    justify-content: center;
  }
  .brand {
    display: flex;
    align-items: center;
    gap: 16px;
  }
  .brand-dot {
    width: 22px;
    height: 22px;
    border-radius: 50%;
    background: var(--pink);
  }
  .brand-name {
    color: var(--pink);
    font-size: 56px;
    font-weight: 400;
    letter-spacing: 1px;
  }
  .tagline {
    margin-top: 10px;
    color: var(--white);
    font-size: 21px;
    font-weight: 300;
    letter-spacing: 2px;
  }

  /* Back side */
  .card-back {
    left: 90px;
    top: 540px;
    background: var(--paper);
  }
  .name-band {
    position: absolute;
    left: 0;
    top: 104px;
    width: 350px;
    height: 90px;
    background: var(--pink);
    color: var(--white);
    padding: 16px 0 0 40px;
  }
  .person-name {
    font-size: 23px;
    font-weight: 700;
  }
  .person-role {
    margin-top: 2px;
    font-size: 18px;
    font-weight: 300;
  }
  .contact {
    position: absolute;
    left: 372px;
    top: 104px;
    color: var(--ink);
    font-size: 19px;
    line-height: 1.2;
    list-style: none;
  }
  .contact li + li { margin-top: 10px; }
  .contact .address { line-height: 1.1; }
</style>
</head>
<body>
<main class="canvas">
  <section class="card card-front" aria-label="Business card front">
    <div class="brand">
      <span class="brand-dot"></span>
      <span class="brand-name">Tiny Brambles</span>
    </div>
    <p class="tagline">Child Care And Kinder</p>
  </section>

  <section class="card card-back" aria-label="Business card back">
    <div class="name-band">
      <p class="person-name">Corinne Helbrook</p>
      <p class="person-role">Director/ Owner</p>
    </div>
    <ul class="contact">
      <li class="address">418 Fernlow Rd<br>Kelmont, 3178</li>
      <li>Phone - 03 9581-4726</li>
      <li>Fax - 03 95814727</li>
      <li>info@tinybrambles.com.au</li>
      <li>www.tinybrambles.com.au</li>
    </ul>
  </section>
</main>
</body>
</html>
```